WEBSITE NEEDED FOR MY COMPANY CALLED BRAVERIDGE HOCKEY DEVELOPMENT

LOOKING FOR A WEBSITE TO MARKET AND SEEL MY HOCKEY DEVELOPMENT PROGRAMS.
NEEDS TO HAVE 5+ PAGES

Target Market(s)

YOUTH SPORTS

Industry/Entity Type

YOUTH ATHLETE DEVELOPMENT

Number of Pages Required

5+ page

Font styles to use
Sans Serif

Colors
0054AA
0677BA
7BADD7
CADEEF
E8F1F8

Requirements
Must have
• MAIN PAGE - SPIRNG PROGRAM PAGE - SUMMER PROGRAM PAGE - WINTER PAGE - TOURNAMENT PAGE
Nice to have
• FLASH
Should not have
• NOT SURE

```html
<!DOCTYPE html>
<html lang="en">
<head>
<meta charset="utf-8">
<title>Braveridge Hockey Development</title>
<link rel="stylesheet" href="https://fonts.googleapis.com/css2?family=Oswald:wght@400;500;600;700&family=Montserrat:wght@400;500;600;700&display=swap">
<style>
:root{
  --navy:#1b2433;
  --navy-deep:#151d2a;
  --blue:#29a8e0;
  --blue-dark:#0677ba;
  --brand:#0054aa;
  --sky:#7badd7;
  --mist:#cadeef;
  --ice:#e8f1f8;
  --teal-mist:#dde9ea;
  --text:#4a4f58;
  --white:#fff;
}
*{margin:0;padding:0;box-sizing:border-box}
html,body{width:1200px;height:5386px;overflow:hidden}
body{position:relative;background:var(--white);font-family:"Montserrat",sans-serif;color:var(--text)}
.abs{position:absolute}
.photo{position:absolute;display:block}

/* header */
.topbar{position:absolute;left:617px;top:0;width:583px;height:22px;background:var(--navy);display:flex;align-items:center;font-size:11px;color:var(--white);font-weight:500}
.topbar .phone{background:var(--blue);height:22px;padding:0 22px 0 28px;display:flex;align-items:center;gap:6px;border-radius:0 0 0 14px}
.topbar .mail{display:flex;align-items:center;gap:6px;margin-left:40px}
.header{position:absolute;left:0;top:0;width:1200px;height:82px}
.logo{position:absolute;left:130px;top:20px;font-family:"Oswald",sans-serif;font-weight:700;font-size:30px;color:var(--blue);letter-spacing:1px}
.nav{position:absolute;left:390px;top:36px;display:flex;gap:34px;font-size:11px;font-weight:700;color:var(--navy);letter-spacing:.3px}
.nav .active{color:var(--blue)}
.btn-book{position:absolute;left:954px;top:37px;width:116px;height:30px;border-radius:15px;background:var(--navy);color:var(--white);font-size:10px;font-weight:700;display:flex;align-items:center;justify-content:center;gap:8px}

/* hero */
.hero{position:absolute;left:0;top:82px;width:1200px;height:728px;background:radial-gradient(ellipse at 62% 35%,#e7eef6 0%,#a8b8c9 28%,#4a5b70 55%,#1f2a3a 80%)}
.hero-fade{position:absolute;left:0;bottom:0;width:1200px;height:220px;background:linear-gradient(rgba(255,255,255,0),#fff)}
.hero-title{position:absolute;left:130px;top:150px;font-family:"Oswald",sans-serif;font-style:italic;font-weight:700;font-size:60px;line-height:70px;color:var(--white);text-transform:uppercase;letter-spacing:-.5px}
.hero-text{position:absolute;left:132px;top:300px;width:340px;font-size:13px;line-height:19px;color:var(--white);font-weight:500}
.btn{display:inline-flex;align-items:center;justify-content:center;gap:8px;font-size:9.5px;font-weight:700;letter-spacing:.4px;color:var(--white);background:var(--blue);text-transform:uppercase}
.hero .btn{position:absolute;left:132px;top:396px;width:126px;height:30px}
.arrow-circle{position:absolute;width:28px;height:28px;border:1.5px solid var(--white);border-radius:50%;display:flex;align-items:center;justify-content:center}
.dots{position:absolute;left:566px;top:560px;display:flex;gap:6px}
.dots i{display:block;width:20px;height:3px;background:var(--navy)}

/* section heading */
.sec-title{position:absolute;left:0;width:1200px;text-align:center;font-family:"Oswald",sans-serif;font-style:italic;font-weight:600;font-size:38px;color:var(--navy);text-transform:uppercase;letter-spacing:-.5px}
.sec-title .slash{display:inline-block;width:3px;height:44px;background:var(--blue);transform:skewX(-22deg);vertical-align:-8px;margin:0 6px}

/* spring grid */
.tile{position:absolute;overflow:hidden}
.tile .cap{position:absolute;left:24px;right:20px;bottom:22px;color:var(--white)}
.tile .cap h4{font-family:"Oswald",sans-serif;font-weight:400;font-size:14px;line-height:20px}
.tile .cap p{font-size:10px;line-height:16px;margin-top:10px;font-weight:500}
.tile .cap .btn{width:116px;height:28px;margin-top:14px}
.shade{position:absolute;inset:0;background:linear-gradient(rgba(20,30,45,0) 40%,rgba(20,30,45,.85))}
.btn-dark{position:absolute;display:flex;align-items:center;justify-content:center;gap:10px;background:var(--navy);color:var(--white);font-size:10px;font-weight:700;text-transform:uppercase;letter-spacing:.2px}

/* welcome + winter */
.intro-h{position:absolute;font-family:"Oswald",sans-serif;font-weight:500;font-size:38px;line-height:44px;color:var(--navy);text-transform:uppercase;letter-spacing:-.5px}
.body-text{position:absolute;font-size:12.5px;line-height:21.5px;color:var(--text)}

/* summer */
.event .inner{position:absolute;left:0;right:0;top:50%;transform:translateY(-50%);text-align:center;color:var(--white)}
.event .date{font-family:"Oswald",sans-serif;font-size:15px;color:var(--blue);font-weight:500}
.event h4{font-family:"Oswald",sans-serif;font-weight:400;font-size:18px;line-height:26px;margin-top:10px}

/* tournament */
.tournament{position:absolute;left:0;top:3058px;width:1200px;height:600px;background:var(--teal-mist)}
.match{position:absolute;top:3230px;width:292px;height:247px;background:var(--white);border-radius:8px;box-shadow:0 2px 10px rgba(0,0,0,.08)}
.match .team{position:absolute;top:30px;width:90px;text-align:center;font-size:10px;line-height:13px;color:var(--navy)}
.match .team .av{width:68px;height:68px;border-radius:50%;margin:0 auto 10px;background:radial-gradient(circle at 50% 40%,#e7703a,#c53d28 60%,#2c4b7a)}
.match .vs{position:absolute;left:0;right:0;top:56px;text-align:center;font-family:"Oswald",sans-serif;font-size:17px;color:var(--blue);font-weight:600}
.match .panel{position:absolute;left:12px;right:12px;top:160px;height:72px;background:var(--ice);border-radius:6px;text-align:center;padding-top:15px}
.match .panel b{font-family:"Oswald",sans-serif;font-weight:400;font-size:12px;color:var(--navy)}
.match .panel p{font-size:10px;line-height:14px;margin-top:6px}
.sq-arrow{position:absolute;width:24px;height:24px;border:1.5px solid #6b7580;display:flex;align-items:center;justify-content:center}

/* newsletter */
.news{position:absolute;left:0;top:4359px;width:1200px;height:529px;background:linear-gradient(90deg,#2a3442 0%,#3c4d63 40%,#6c7f98 65%,#8e3b3f 85%,#3a4c70 100%)}
.news-panel{position:absolute;left:0;top:4470px;width:600px;height:330px;background:linear-gradient(90deg,rgba(21,29,42,.85),rgba(21,29,42,.2))}
.news-h{position:absolute;left:130px;font-family:"Oswald",sans-serif;font-weight:500;color:var(--white)}
.field{position:absolute;left:130px;top:4666px;width:347px;height:34px;background:var(--white);font-size:10px;color:#888;padding:11px 18px}

/* footer */
.footer{position:absolute;left:0;top:4888px;width:1200px;height:498px;background:var(--navy)}
.f-logo{position:absolute;left:130px;top:5010px;font-family:"Oswald",sans-serif;font-weight:700;font-size:50px;color:var(--blue);letter-spacing:1px}
.f-head{position:absolute;top:4978px;font-family:"Oswald",sans-serif;font-weight:500;font-size:14px;color:var(--white);text-transform:uppercase}
.f-text{position:absolute;font-size:10.5px;line-height:18px;color:#d0d6de}
.f-row{display:flex;gap:16px;align-items:flex-start;margin-bottom:14px}
.socials{position:absolute;left:519px;top:5256px;display:flex;gap:6px}
.socials i{display:block;width:26px;height:26px;border:1.5px solid var(--white);border-radius:50%}
.copy{position:absolute;left:0;top:5310px;width:1200px;text-align:center;font-size:12px;color:#d0d6de}
</style>
</head>
<body>

<!-- header -->
<header class="header">
  <div class="logo">BRAVERIDGE</div>
  <nav class="nav">
    <span class="active">HOME</span><span>SPRING PROGRAM</span><span>SUMMER PROGRAM</span><span>WINTER</span><span>TOURNAMENT</span>
  </nav>
  <div class="btn-book">BOOK NOW
    <svg width="14" height="8" viewBox="0 0 14 8"><path d="M0 4h12M9 1l3 3-3 3" stroke="#fff" stroke-width="1.4" fill="none"/></svg>
  </div>
</header>
<div class="topbar">
  <div class="phone">
    <svg width="10" height="10" viewBox="0 0 10 10"><path d="M2 1l2 2-1 1.2a6 6 0 0 0 2.8 2.8L7 6l2 2-1.2 1.4C4.5 9.4.6 5.5.6 2.2z" fill="#fff"/></svg>
    +1(555) 0142-7731
  </div>
  <div class="mail">
    <svg width="11" height="8" viewBox="0 0 11 8"><rect width="11" height="8" fill="#fff"/><path d="M0 0l5.5 4.5L11 0" stroke="#1b2433" fill="none"/></svg>
    info@braveridgehockey.com
  </div>
</div>

<!-- hero -->
<section class="hero">
  <div class="photo" role="img" aria-label="Hockey players racing for the puck on bright ice" style="inset:0"></div>
  <div class="hero-fade"></div>
  <h1 class="hero-title">BRAVERIDGE HOCKEY<br>DEVELOPMENT</h1>
  <p class="hero-text">Lorem ipsum dolor sit amet, consectetur adipiscing elit, sed do eiusmod tempor incididunt ut labore et dolore magna aliqua. Ut enim ad minim veniam, quis nostrud exercitation ullamco</p>
  <span class="btn">LEARN MORE
    <svg width="14" height="8" viewBox="0 0 14 8"><path d="M0 4h12M9 1l3 3-3 3" stroke="#fff" stroke-width="1.4" fill="none"/></svg></span>
  <div class="arrow-circle" style="left:68px;top:251px"><svg width="12" height="10" viewBox="0 0 12 10"><path d="M12 5H2M5 1L1 5l4 4" stroke="#fff" stroke-width="1.4" fill="none"/></svg></div>
  <div class="arrow-circle" style="left:1102px;top:251px"><svg width="12" height="10" viewBox="0 0 12 10"><path d="M0 5h10M7 1l4 4-4 4" stroke="#fff" stroke-width="1.4" fill="none"/></svg></div>
  <div class="dots"><i></i><i></i><i></i></div>
</section>

<h2 class="sec-title" style="top:750px">SPRING<span class="slash"></span>PROGRAM</h2>

<!-- spring grid -->
<div class="tile" style="left:130px;top:849px;width:384px;height:485px">
  <div class="photo" role="img" aria-label="Two players skating hard through shattering ice" style="inset:0;background:linear-gradient(160deg,#c9d6e3,#6d7f95 45%,#2b3748)"></div>
  <div class="shade"></div>
  <div class="cap" style="bottom:26px">
    <h4>Excepteur sint occaecat cupidatat non<br>proident, sunt in culpa</h4>
    <p>Lorem ipsum dolor sit amet, consectetur adipiscing elit, sed do eiusmod tempor incididunt ut labore et dolore magna aliqua.</p>
    <span class="btn">LEARN MORE <svg width="14" height="8" viewBox="0 0 14 8"><path d="M0 4h12M9 1l3 3-3 3" stroke="#fff" stroke-width="1.4" fill="none"/></svg></span>
  </div>
</div>
<div class="tile" style="left:523px;top:849px;width:267px;height:236px">
  <div class="photo" role="img" aria-label="Youth players in red jerseys at a faceoff" style="inset:0;background:linear-gradient(160deg,#3d5474,#7b3a3c 55%,#1f2836)"></div>
  <div class="shade"></div>
  <div class="cap"><h4>Excepteur sint occaecat cupidatat non proident, sunt in culpa</h4></div>
</div>
<div class="tile" style="left:801px;top:849px;width:267px;height:236px">
  <div class="photo" role="img" aria-label="Young team gathered at the bench" style="inset:0;background:linear-gradient(160deg,#4c6078,#8a3234 55%,#1f2836)"></div>
  <div class="shade"></div>
  <div class="cap"><h4>Excepteur sint occaecat cupidatat non proident, sunt in culpa</h4></div>
</div>
<div class="tile" style="left:523px;top:1095px;width:267px;height:239px">
  <div class="photo" role="img" aria-label="Youth players in orange and blue chasing the puck" style="inset:0;background:linear-gradient(160deg,#6aa0c9,#d0692e 50%,#2a3647)"></div>
  <div class="shade"></div>
  <div class="cap"><h4>Excepteur sint occaecat cupidatat non proident, sunt in culpa</h4></div>
</div>
<div class="tile" style="left:801px;top:1095px;width:267px;height:239px">
  <div class="photo" role="img" aria-label="Wide view of an indoor rink during a game" style="inset:0;background:linear-gradient(180deg,#1f2b40,#c8d3df 50%,#5a6a80)"></div>
  <div class="shade"></div>
  <div class="cap"><h4>Excepteur sint occaecat cupidatat non proident, sunt in culpa</h4></div>
</div>

<div class="btn-dark" style="left:506px;top:1386px;width:188px;height:36px">VIEW ALL SPRING PROGRAM
  <svg width="14" height="8" viewBox="0 0 14 8"><path d="M0 4h12M9 1l3 3-3 3" stroke="#fff" stroke-width="1.4" fill="none"/></svg></div>

<!-- welcome -->
<svg class="abs" style="left:130px;top:1532px" width="560" height="490" viewBox="0 0 560 490" role="img" aria-label="Player in white driving toward the puck under arena lights">
  <defs><linearGradient id="g1" x1="0" y1="0" x2="1" y2="1"><stop offset="0" stop-color="#2f6fb7"/><stop offset=".5" stop-color="#a9c7e6"/><stop offset="1" stop-color="#1d3253"/></linearGradient></defs>
  <path d="M0 0H480L560 110 440 482H0Z" fill="url(#g1)"/>
</svg>
<h2 class="intro-h" style="left:742px;top:1588px">WELCOME TO<br>BRAVERIDGE HOCKEY<br>DEVELOPMENT</h2>
<p class="body-text" style="left:742px;top:1730px;width:340px">Lorem ipsum dolor sit amet, consectetur adipiscing elit, sed do eiusmod tempor incididunt ut labore et dolore magna aliqua. Ut enim ad minim veniam, quis nostrud exercitation ullamco laboris nisi ut aliquip ex ea commodo consequat. Duis aute irure dolor in reprehenderit in voluptate velit esse cillum dolore eu fugiat nulla pariatur. Excepteur sint occaecat cupidatat non proident, sunt in culpa qui officia deserunt mollit anim id est laborum.</p>
<span class="btn abs" style="left:742px;top:1927px;width:124px;height:30px">LEARN MORE <svg width="14" height="8" viewBox="0 0 14 8"><path d="M0 4h12M9 1l3 3-3 3" stroke="#fff" stroke-width="1.4" fill="none"/></svg></span>

<!-- summer -->
<h2 class="sec-title" style="top:2140px">SUMMER<span class="slash"></span>PROGRAM</h2>

<div class="tile event" style="left:0;top:2254px;width:400px;height:402px">
  <div class="photo" role="img" aria-label="Players battling at a faceoff" style="inset:0;background:linear-gradient(160deg,#4e5a68,#6d3539 50%,#1f2733)"></div>
  <div class="photo" style="inset:0;background:rgba(20,28,40,.45)"></div>
  <div class="inner"><div class="date">AUGUST 02 2022</div><h4>Excepteur sint occaecat cupidatat non<br>proident, sunt in culpa</h4></div>
</div>
<div class="tile event" style="left:400px;top:2254px;width:400px;height:402px">
  <div class="photo" role="img" aria-label="Young players in helmets on the bench" style="inset:0;background:linear-gradient(160deg,#5cb8e4,#2f97cf 60%,#3a88b8)"></div>
  <div class="inner"><div class="date" style="color:#fff">AUGUST 02 2022</div><h4>Excepteur sint occaecat cupidatat non<br>proident, sunt in culpa</h4></div>
</div>
<div class="tile event" style="left:800px;top:2254px;width:400px;height:402px">
  <div class="photo" role="img" aria-label="Player handling the puck in dim arena light" style="inset:0;background:linear-gradient(160deg,#3f4a57,#2a323d 60%,#1b222c)"></div>
  <div class="inner"><div class="date">AUGUST 02 2022</div><h4>Excepteur sint occaecat cupidatat non<br>proident, sunt in culpa</h4></div>
</div>
<div class="tile event" style="left:0;top:2656px;width:400px;height:402px">
  <div class="photo" role="img" aria-label="Skater crossing the ice in front of the stands" style="inset:0;background:linear-gradient(160deg,#2d4058,#243244 60%,#1a2330)"></div>
  <div class="inner"><div class="date">AUGUST 02 2022</div><h4>Excepteur sint occaecat cupidatat non<br>proident, sunt in culpa</h4></div>
</div>
<div class="tile event" style="left:400px;top:2656px;width:800px;height:402px">
  <div class="photo" role="img" aria-label="Player in a dark jersey taking a shot, puck in flight" style="inset:0;background:linear-gradient(110deg,#263a52,#4b6683 45%,#2d4560 75%,#1e2f44)"></div>
  <div class="inner" style="left:400px;top:66%"><div class="date">AUGUST 02 2022</div><h4>Excepteur sint occaecat cupidatat non<br>proident, sunt in culpa</h4></div>
</div>

<!-- tournament -->
<section class="tournament"></section>
<h2 class="sec-title" style="top:3122px">OUR<span class="slash"></span>TOURNAMENT</h2>
<div class="sq-arrow" style="left:76px;top:3337px"><svg width="12" height="10" viewBox="0 0 12 10"><path d="M12 5H2M5 1L1 5l4 4" stroke="#6b7580" stroke-width="1.4" fill="none"/></svg></div>
<div class="sq-arrow" style="left:1098px;top:3337px"><svg width="12" height="10" viewBox="0 0 12 10"><path d="M0 5h10M7 1l4 4-4 4" stroke="#6b7580" stroke-width="1.4" fill="none"/></svg></div>

<div class="match" style="left:130px">
  <div class="team" style="left:28px"><div class="av" role="img" aria-label="Team photo"></div>Excepteur sint<br>occaecat</div>
  <div class="vs">VS</div>
  <div class="team" style="right:28px"><div class="av" role="img" aria-label="Team photo"></div>Excepteur sint<br>occaecat</div>
  <div class="panel"><b>August 2 2022</b><p>Lorem ipsum dolor sit amet,<br>consectetur adipiscing</p></div>
</div>
<div class="match" style="left:454px">
  <div class="team" style="left:28px"><div class="av" role="img" aria-label="Team photo"></div>Excepteur sint<br>occaecat</div>
  <div class="vs">VS</div>
  <div class="team" style="right:28px"><div class="av" role="img" aria-label="Team photo"></div>Excepteur sint<br>occaecat</div>
  <div class="panel"><b>August 2 2022</b><p>Lorem ipsum dolor sit amet,<br>consectetur adipiscing</p></div>
</div>
<div class="match" style="left:778px">
  <div class="team" style="left:28px"><div class="av" role="img" aria-label="Team photo"></div>Excepteur sint<br>occaecat</div>
  <div class="vs">VS</div>
  <div class="team" style="right:28px"><div class="av" role="img" aria-label="Team photo"></div>Excepteur sint<br>occaecat</div>
  <div class="panel"><b>August 2 2022</b><p>Lorem ipsum dolor sit amet,<br>consectetur adipiscing</p></div>
</div>
<div class="btn-dark" style="left:506px;top:3533px;width:188px;height:38px">VIEW ALL TOURNAMENT
  <svg width="14" height="8" viewBox="0 0 14 8"><path d="M0 4h12M9 1l3 3-3 3" stroke="#fff" stroke-width="1.4" fill="none"/></svg></div>

<!-- winter -->
<h2 class="intro-h" style="left:130px;top:3858px">BRAVERIDGE HOCKEY<br>WINTER</h2>
<p class="body-text" style="left:130px;top:3962px;width:340px">Lorem ipsum dolor sit amet, consectetur adipiscing elit, sed do eiusmod tempor incididunt ut labore et dolore magna aliqua. Ut enim ad minim veniam, quis nostrud exercitation ullamco laboris nisi ut aliquip ex ea commodo consequat. Duis aute irure dolor in reprehenderit in voluptate velit esse cillum dolore eu fugiat nulla pariatur. Excepteur sint occaecat cupidatat non proident, sunt in culpa qui officia deserunt mollit anim id est laborum.</p>
<span class="btn abs" style="left:130px;top:4160px;width:124px;height:30px">LEARN MORE <svg width="14" height="8" viewBox="0 0 14 8"><path d="M0 4h12M9 1l3 3-3 3" stroke="#fff" stroke-width="1.4" fill="none"/></svg></span>
<svg class="abs" style="left:548px;top:3763px" width="522" height="486" viewBox="0 0 522 486" role="img" aria-label="Player in yellow shooting at the goal net">
  <defs><linearGradient id="g2" x1="0" y1="0" x2="1" y2="1"><stop offset="0" stop-color="#5a1d22"/><stop offset=".45" stop-color="#c9b24a"/><stop offset=".7" stop-color="#9fb3c8"/><stop offset="1" stop-color="#2c3d55"/></linearGradient></defs>
  <path d="M80 0H522V480H170L0 190Z" fill="url(#g2)"/>
</svg>

<!-- newsletter -->
<section class="news" role="img" aria-label="Coach and goaltender at a rink, masks and gear in view"></section>
<div class="news-panel"></div>
<div class="news-h" style="top:4508px;font-size:30px">Stay Connected</div>
<div class="news-h" style="top:4552px;font-size:36px"><span style="color:var(--blue)">JOIN</span> OUR NEWSLETTER</div>
<p class="abs" style="left:130px;top:4612px;width:330px;font-family:'Oswald',sans-serif;font-size:12px;line-height:18px;color:#d0d6de">Stay up to date with all the latest news, events and Lorem ipsum dolor sit amet, consectetur adipiscing</p>
<div class="field">Enter your email</div>
<span class="btn abs" style="left:130px;top:4719px;width:154px;height:35px">SUBSCRIBE <svg width="14" height="8" viewBox="0 0 14 8"><path d="M0 4h12M9 1l3 3-3 3" stroke="#fff" stroke-width="1.4" fill="none"/></svg></span>

<!-- footer -->
<footer class="footer"></footer>
<div class="f-logo">BRAVERIDGE</div>
<div class="f-head" style="left:439px">CONTACT US</div>
<p class="f-text" style="left:439px;top:5010px;width:180px">Lorem ipsum dolor sit amet, consectetur adipiscing elit, sed do eiusmod tempor incididunt ut labore et dolore magna aliqua. Ut enim ad minim veniam, quis nostrud exeration ullamco laboris</p>
<div class="f-head" style="left:673px">CONTACT US</div>
<div class="f-text" style="left:673px;top:5014px;width:260px">
  <div class="f-row"><svg width="12" height="11" viewBox="0 0 12 11"><path d="M0 11V4l4-2v2l4-2v9Z M9 11V1h3v10Z" fill="#fff"/></svg><span>Braveridge Hockey Development<br>275 Lorem ipsum dolor sit amet,<br>consectetur adipiscing</span></div>
  <div class="f-row"><svg width="11" height="11" viewBox="0 0 10 10"><path d="M2 1l2 2-1 1.2a6 6 0 0 0 2.8 2.8L7 6l2 2-1.2 1.4C4.5 9.4.6 5.5.6 2.2z" fill="#fff"/></svg><span>+1(555) 0142-7731</span></div>
  <div class="f-row"><svg width="12" height="9" viewBox="0 0 11 8"><rect width="11" height="8" fill="#fff"/><path d="M0 0l5.5 4.5L11 0" stroke="#1b2433" fill="none"/></svg><span>info@braveridgehockey.com</span></div>
</div>
<div class="f-head" style="left:976px">QUICK LINKS</div>
<p class="f-text" style="left:976px;top:5014px;line-height:22px">Spring Program<br>Summer Program<br>Winter<br>Tournament</p>
<div class="socials"><i></i><i></i><i></i><i></i><i></i></div>
<p class="copy">Copyright © Braveridge Hockey Development 2022. All rights reserved.</p>

</body>
</html>
```